Business Card, Stationary with Shark Logo for Personal Injury Lawyer

I need business cards and stationery with a shark logo for my Personal Injury Law Practice. Has to have this written on it:
Martin K. Hollis
Injury Lawyer
The Corvell Building
718 Tandy Street
Providence, Rhode Island 02908
401-627-4193
Martinhollis.com

Contact Information for Business Card

Martin K. Hollis, Injury Lawyer, address, 401-627-4193, martinhollis.com

```html
<!DOCTYPE html>
<html lang="en">
<head>
<meta charset="utf-8">
<title>Martin K. Hollis – Injury Lawyer – Business Card</title>
<link rel="stylesheet" href="https://fonts.googleapis.com/css2?family=Montserrat:wght@700;800&display=swap">
<style>
  :root {
    --navy: #1b1a6b;
    --ocean: #1d8fd8;
    --sky: #35b8ee;
    --ink: #000000;
    --slate: #3c3d78;
    --paper: #ffffff;
    --frame: #1a1a1a;
  }
  * { margin: 0; padding: 0; box-sizing: border-box; }
  html, body {
    width: 1200px;
    height: 669px;
    overflow: hidden;
    background: var(--paper);
  }
  .card {
    position: relative;
    width: 1200px;
    height: 669px;
    background: var(--paper);
    border: 2px solid var(--frame);
    overflow: hidden;
    font-family: "Montserrat", Arial, sans-serif;
    font-weight: 700;
  }
  .mascot-panel {
    position: absolute;
    left: 0;
    top: 0;
    width: 530px;
    height: 669px;
  }
  .brand {
    position: absolute;
    right: 74px;
    top: 44px;
    display: flex;
    align-items: center;
    gap: 22px;
  }
  .brand-mark {
    width: 64px;
    height: 64px;
    background: var(--navy);
    flex: none;
  }
  .brand-name {
    color: var(--navy);
    font-weight: 800;
    text-align: right;
    text-transform: uppercase;
    line-height: 0.95;
    letter-spacing: -1px;
  }
  .brand-name .first { display: block; font-size: 56px; }
  .brand-name .last { display: block; font-size: 96px; }
  .identity {
    position: absolute;
    right: 74px;
    top: 262px;
    text-align: right;
    font-size: 34px;
    line-height: 1.22;
  }
  .identity .person { color: var(--ink); }
  .identity .role { color: var(--slate); }
  .address {
    position: absolute;
    right: 74px;
    top: 368px;
    text-align: right;
    color: var(--slate);
    font-size: 24px;
    line-height: 1.35;
    font-style: normal;
  }
  .contact {
    position: absolute;
    right: 74px;
    top: 488px;
    text-align: right;
    color: var(--ink);
    font-size: 30px;
    line-height: 1.27;
  }
</style>
</head>
<body>
  <main class="card">
    <svg class="mascot-panel" viewBox="0 0 530 669" role="img" aria-label="Shark logo mascot illustration in blue tones on a slanted navy band">
      <defs>
        <linearGradient id="panelFade" x1="0" y1="0" x2="1" y2="0">
          <stop offset="0" stop-color="#35b8ee"/>
          <stop offset="0.45" stop-color="#1d8fd8"/>
          <stop offset="1" stop-color="#1b1a6b"/>
        </linearGradient>
      </defs>
      <polygon points="0,0 400,0 530,669 0,669" fill="url(#panelFade)"/>
    </svg>

    <div class="brand">
      <span class="brand-mark" aria-hidden="true"></span>
      <p class="brand-name"><span class="first">Martin K.</span><span class="last">Hollis</span></p>
    </div>

    <div class="identity">
      <p class="person">Martin K. Hollis</p>
      <p class="role">Injury Lawyer</p>
    </div>

    <address class="address">
      <p>The Corvell Building</p>
      <p>718 Tandy Street</p>
      <p>Providence, Rhode Island 02908</p>
    </address>

    <div class="contact">
      <p class="phone">401-627-4193</p>
      <p class="email">martin@martinhollis.com</p>
      <p class="web">martinhollis.com</p>
    </div>
  </main>
</body>
</html>
```